Christmas Party Poster

I am promoting a Christmas Party for teenagers age 13-17 years old. The event is the first of its kind in our area, Weston Super Mare. The ticket price is to include food, soft drink's, music, entertainment.

There is nothing else of its kind in the the area or surrounding towns so a one of a kind event and new to the town. I would like the poster to be as simple and less busy as possible while still clearly showing the key information, anything that can be added it to show its a Christmas party for teenagers would be great. Also this is aimed at 13-17 year old's so as current and modern a design as possible.
Updates

A big thank you for the designs so far, As this is my first project I'm just getting the hang of what to ask for. I have slightly updated the brief and I now realize less is more, so long as the poster has the key elements of event name, date, time's, location, price and age range. The rest I should have been more flexible on. Thank you for your patience.

Target Market(s)

My Target Market are teenagers specifically 13-17 year olds

Industry/Entity Type

Town

Requirements
Must have
• The Title 'Frostgleam' The venue is 'The Amber Pavilion h-b-t', Phone Number '01852 630284' Date '19th December'. Times '19.00 - 23.00'. Strictly u18 or age 13-17 years. Ticket price of £20. Face book 'frost gleam hbt' limited 4 tickets per person
Nice to have
• Christmas Party, Photo of your night out. Food and drink included
Should not have
• no worded reference to Santa, snowmen, reindeer, disco, try to keep out as not to offend cool teenagers.

```html
<!DOCTYPE html>
<html lang="en">
<head>
<meta charset="utf-8">
<title>Frostgleam – Christmas Party Poster</title>
<link rel="stylesheet" href="https://fonts.googleapis.com/css2?family=Schoolbell&family=Walter+Turncoat&family=Sue+Ellen+Francisco&display=swap">
<style>
  :root {
    --stage: #d9d9d9;
    --night: #141414;
    --night-soft: #262626;
    --ice-cyan: #3ee0ea;
    --sky-blue: #3aa6e0;
    --frost-white: #ececec;
    --band-grey: #7c7c7c;
    --sea-teal: #33c2ac;
  }
  * { box-sizing: border-box; margin: 0; padding: 0; }
  html, body {
    width: 1200px;
    height: 700px;
    overflow: hidden;
    background: var(--stage);
  }
  .canvas {
    position: relative;
    width: 1200px;
    height: 700px;
    display: flex;
    align-items: center;
    justify-content: center;
  }
  .poster {
    position: relative;
    width: 460px;
    height: 640px;
    overflow: hidden;
    box-shadow: 0 6px 22px rgba(0,0,0,0.25);
  }
  .poster__texture {
    position: absolute;
    inset: 0;
    background: radial-gradient(ellipse at 50% 40%, var(--night-soft), var(--night) 75%);
  }
  .poster__content {
    position: relative;
    height: 100%;
    display: flex;
    flex-direction: column;
    align-items: center;
    text-align: center;
  }
  .kicker {
    margin-top: 34px;
    font-family: "Walter Turncoat", cursive;
    font-size: 21px;
    letter-spacing: 1px;
    color: var(--sky-blue);
  }
  .event-title {
    margin-top: 2px;
    font-family: "Schoolbell", cursive;
    font-weight: 400;
    font-size: 78px;
    line-height: 1;
    color: var(--frost-white);
  }
  .date-band {
    margin-top: 26px;
    width: 100%;
    height: 62px;
    background: var(--band-grey);
    display: flex;
    align-items: center;
    justify-content: center;
    font-family: "Schoolbell", cursive;
    font-size: 36px;
    color: var(--frost-white);
  }
  .venue {
    margin-top: 22px;
    font-family: "Walter Turncoat", cursive;
    font-size: 23px;
    color: var(--ice-cyan);
  }
  .divider {
    margin-top: 12px;
    width: 320px;
    height: 2px;
    background: var(--sky-blue);
  }
  .times {
    margin-top: 18px;
    font-family: "Walter Turncoat", cursive;
    font-size: 30px;
    color: var(--ice-cyan);
  }
  .age {
    margin-top: 4px;
    font-family: "Walter Turncoat", cursive;
    font-size: 18px;
    color: var(--ice-cyan);
  }
  .price {
    margin-top: 4px;
    display: flex;
    align-items: baseline;
    gap: 10px;
    color: var(--ice-cyan);
  }
  .price__amount {
    font-family: "Schoolbell", cursive;
    font-size: 58px;
    line-height: 1;
  }
  .price__label {
    font-family: "Walter Turncoat", cursive;
    font-size: 18px;
  }
  .inclusions {
    margin-top: 4px;
    font-family: "Walter Turncoat", cursive;
    font-size: 18px;
    color: var(--ice-cyan);
  }
  .contact {
    margin-top: 30px;
    display: flex;
    align-items: baseline;
    gap: 12px;
    color: var(--sea-teal);
  }
  .contact__label {
    font-family: "Walter Turncoat", cursive;
    font-size: 14px;
    color: var(--ice-cyan);
  }
  .contact__phone {
    font-family: "Sue Ellen Francisco", cursive;
    font-size: 50px;
    line-height: 1;
    letter-spacing: 2px;
  }
</style>
</head>
<body>
  <main class="canvas">
    <article class="poster">
      <div class="poster__texture" role="img" aria-label="Night sky with falling snowflakes"></div>
      <div class="poster__content">
        <p class="kicker">CRISTMAS PARTY</p>
        <h1 class="event-title">Frostgleam</h1>
        <p class="date-band">19th December</p>
        <p class="venue">The Amber Pavilion H-B-T</p>
        <div class="divider"></div>
        <p class="times">FROM 19.00 TO 23.00</p>
        <p class="age">AGE 13-17</p>
        <p class="price">
          <span class="price__amount">£20</span>
          <span class="price__label">ticket</span>
        </p>
        <p class="inclusions">Food and drink included</p>
        <p class="contact">
          <span class="contact__label">call us</span>
          <span class="contact__phone">01852 630284</span>
        </p>
      </div>
    </article>
  </main>
</body>
</html>
```